HARD MONEY ORIGINATOR RECRUITMENT.
Looking for individuals to help us originate loans for real estate investor financing primarily used to fix up properties and resell.
HARD MONEY ORIGINATORS WANTED
No Licensing Required
Work As Independent Contractor
1% Flat Finders Fee on Each Loan
Referral Compensation for Recruiting New Originators
Immediate Payouts
Programs Offered Nationwide
Marketing Assistance and Support Available
Email mpelton@brightquaylending.com for more information or call (800) 641-2950 Ext. 24 Brightquay Lending Services, Inc. www.brightquaylending.com NMLS #318760
Industry/Entity Type
Real Estate
Look and feel
Each slider illustrates characteristics of the customer's brand and the style your logo design should communicate.

```html
<!DOCTYPE html>
<html lang="en">
<head>
<meta charset="utf-8">
<title>Hard Money Originators Wanted – Brightquay Lending Services</title>
<link href="https://fonts.googleapis.com/css2?family=Source+Sans+3:wght@400;600;700&family=Roboto+Condensed:wght@700&display=swap" rel="stylesheet">
<style>
  :root{
    --bg:#6b6b6b;
    --navy:#1b4f8f;
    --navy-dark:#123a6e;
    --gold:#b39a22;
    --green:#8cc63f;
    --green-dark:#6ea52a;
    --panel-gray:#e9e7ea;
    --white:#ffffff;
    --text-dark:#2c2c2c;
  }
  *{box-sizing:border-box;margin:0;padding:0}
  html,body{width:1200px;height:1200px;overflow:hidden}
  body{background:var(--bg);font-family:"Source Sans 3",Arial,sans-serif}
  .flyer{position:absolute;left:221px;top:63px;width:758px;height:1074px;background:var(--white);overflow:hidden}
  .flyer-art{position:absolute;inset:0}
  .brand{position:absolute;left:40px;top:150px;display:flex;align-items:center;gap:10px}
  .brand-mark{width:22px;height:22px;background:var(--navy)}
  .brand-name{font-weight:700;font-size:15px;color:var(--navy);line-height:1.1;width:190px}
  .intro{position:absolute;left:39px;top:400px;width:284px;text-align:center;color:var(--white)}
  .intro-title{font-weight:700;font-size:18px;line-height:28px;letter-spacing:.2px}
  .btn{display:block;margin:0 auto;border-radius:14px;background:linear-gradient(var(--green),var(--green-dark));color:var(--white);font-weight:700;box-shadow:0 2px 3px rgba(0,0,0,.3)}
  .btn-join{width:205px;height:32px;line-height:32px;font-size:18px;margin-top:14px}
  .intro-copy{text-align:left;font-size:13px;line-height:17px;padding:0 22px;margin-top:14px}
  .btn-apply{width:156px;height:25px;line-height:25px;font-size:11.5px;margin-top:18px;font-weight:600}
  .headline{position:absolute;left:340px;top:402px;width:400px;text-align:center;font-weight:700;font-size:29px;line-height:39px}
  .headline .l1{color:var(--navy)}
  .headline .l2{color:var(--gold)}
  .headline-rule{position:absolute;left:402px;top:483px;width:275px;height:3px;background:var(--navy)}
  .perk{position:absolute;background:var(--white);border:2px solid var(--navy);padding:3px;box-shadow:0 1px 3px rgba(0,0,0,.25)}
  .perk span{display:flex;align-items:center;justify-content:center;width:100%;height:100%;border:1px solid #8aa3c6;text-align:center;font-weight:600;font-size:13.5px;line-height:18px;color:var(--text-dark);padding:0 8px}
  .perk-wide span{padding:0 14px}
  .contact{position:absolute;right:32px;top:860px;text-align:right;color:var(--white)}
  .call-label{font-family:"Roboto Condensed",Arial,sans-serif;font-weight:700;font-size:31px;line-height:38px}
  .call-number{font-weight:700;font-size:27px;line-height:36px;margin-top:2px}
  .info-pill{display:inline-block;margin-top:6px;background:var(--gold);border-radius:14px;padding:0 14px;height:28px;line-height:28px;font-weight:700;font-size:17px}
  .contact-line{font-weight:700;font-size:15px;line-height:24px}
</style>
</head>
<body>
<div class="flyer">
  <svg class="flyer-art" width="758" height="1074" viewBox="0 0 758 1074">
    <defs>
      <linearGradient id="photoTone" x1="0" y1="0" x2="1" y2="1">
        <stop offset="0" stop-color="#f4f2ee"/>
        <stop offset=".55" stop-color="#d9c7ad"/>
        <stop offset="1" stop-color="#8e8174"/>
      </linearGradient>
      <linearGradient id="panelBlue" x1="0" y1="0" x2="0" y2="1">
        <stop offset="0" stop-color="#1f5a9e"/>
        <stop offset="1" stop-color="#123a6e"/>
      </linearGradient>
      <linearGradient id="workerTone" x1="0" y1="0" x2="0" y2="1">
        <stop offset="0" stop-color="#3a69a8"/>
        <stop offset="1" stop-color="#7a4f4a"/>
      </linearGradient>
      <radialGradient id="cashTone">
        <stop offset="0" stop-color="#e9e4dc"/>
        <stop offset="1" stop-color="#9aa58c"/>
      </radialGradient>
    </defs>

    <path role="img" aria-label="Photo of two professionals reviewing a clipboard in a bright renovated interior" fill="url(#photoTone)"
      d="M0 0H758V330C640 330 520 360 400 392C360 400 330 402 300 402H0Z"/>
    <path fill="none" stroke="var(--gold)" stroke-width="6" d="M0 240C20 300 40 340 60 360"/>

    <path fill="var(--navy)" d="M323 402C470 352 620 312 758 332V480C735 410 680 372 600 372C520 372 420 385 323 405Z"/>
    <path fill="none" stroke="var(--gold)" stroke-width="4" d="M440 382C540 364 640 366 690 384C725 400 745 440 756 490"/>

    <path fill="url(#panelBlue)" d="M39 326Q39 314 52 316C140 330 240 380 323 402V862Q323 872 313 872H49Q39 872 39 862Z"/>
    <rect role="img" aria-label="Photo of a smiling construction worker carrying lumber in front of a house" x="39" y="660" width="284" height="212" rx="8" fill="url(#workerTone)"/>

    <rect x="343" y="530" width="392" height="244" fill="var(--panel-gray)"/>
    <g fill="none" stroke="var(--gold)" stroke-width="2">
      <path d="M343 530V774H735V530"/>
      <path d="M411 598V629M539 598V629M669 598V629M411 715V744"/>
      <path d="M343 530H356M735 530H724"/>
    </g>
    <g fill="var(--gold)">
      <path d="M338 575L348 575L343 583Z"/>
      <path d="M338 690L348 690L343 698Z"/>
      <path d="M520 769L528 774L520 779Z"/>
      <path d="M640 769L648 774L640 779Z"/>
      <path d="M730 585L740 585L735 577Z"/>
      <path d="M730 740L740 740L735 732Z"/>
    </g>

    <path fill="var(--gold)" d="M0 880C120 800 300 880 420 860C560 836 660 792 758 790V1074H0Z"/>
    <path fill="var(--navy)" d="M0 930C140 866 300 922 440 886C580 850 680 818 758 814V1074H0Z"/>
    <path fill="var(--white)" d="M0 900C100 860 220 905 320 905C260 950 120 960 0 1000Z"/>

    <circle cx="211" cy="946" r="114" fill="var(--gold)"/>
    <circle cx="211" cy="946" r="106" fill="var(--white)"/>
    <circle role="img" aria-label="Illustration of a small house sitting on stacks of cash" cx="211" cy="946" r="96" fill="url(#cashTone)"/>
  </svg>

  <div class="brand">
    <div class="brand-mark"></div>
    <div class="brand-name">Brightquay Lending Services, Inc.</div>
  </div>

  <section class="intro">
    <h2 class="intro-title">ARE YOU A<br>MORTGAGE PROFESSIONAL?</h2>
    <div class="btn btn-join">JOIN OUR TEAM!</div>
    <p class="intro-copy">At Brightquay Lending Services, Inc. we pay our Mortgage Consultants the MOST and require the LEAST. We only ask that our Mortgage Consultants generate workable and complete loan applications</p>
    <div class="btn btn-apply">Apply Now</div>
  </section>

  <h1 class="headline"><span class="l1">HARD MONEY</span><br><span class="l2">ORIGINATORS WANTED</span></h1>
  <div class="headline-rule"></div>

  <div class="perk" style="left:356px;top:512px;width:110px;height:86px"><span>No Licensing Required</span></div>
  <div class="perk" style="left:484px;top:512px;width:110px;height:86px"><span>Work As Independent Contractor</span></div>
  <div class="perk" style="left:614px;top:512px;width:110px;height:86px"><span>1% Flat Finders Fee on Each Loan</span></div>
  <div class="perk" style="left:356px;top:629px;width:110px;height:86px"><span>Immediate Payouts</span></div>
  <div class="perk" style="left:484px;top:629px;width:110px;height:86px"><span>Marketing Assistance &amp; Support Available</span></div>
  <div class="perk" style="left:614px;top:629px;width:110px;height:86px"><span>Programs Offered Nationwide</span></div>
  <div class="perk perk-wide" style="left:356px;top:744px;width:134px;height:104px"><span>Referral Compensation for Recruiting New Originators</span></div>

  <section class="contact">
    <div class="call-label">CALL US :</div>
    <div class="call-number">(800) 641-2950 Ext. 24</div>
    <div class="info-pill">FOR MORE INFORMATION :</div>
    <div class="contact-line">Email: mpelton@brightquaylending.com</div>
    <div class="contact-line">www.brightquaylending.com</div>
    <div class="contact-line">NMLS #318760</div>
  </section>
</div>
</body>
</html>
```